We are a Dog Treat company that is going to sell a product that can be served frozen or room temp

Think about something similar to the mandarin oranges cups sold by vurtan. Our product needs to be sealed tight to maintain freshness. We want to sell the product in packs of 4, so a package would have 4 individual cups.
Each cup will contain around 3.5 ounces of product.

I have uploaded some packaging examples, and I uploaded our logo.

Target Market(s)

Dog owners, brelko users, people who purchase dog food online

Industry/Entity Type

It Company

Requirements
Must have
• vacuum seal, logo on box
Nice to have
• logo on each cup

```html
<!DOCTYPE html>
<html lang="en">
<head>
<meta charset="utf-8">
<title>Duo Doxie Dog Treats – Box Dieline</title>
<link rel="stylesheet" href="https://fonts.googleapis.com/css2?family=Courgette&family=Dancing+Script:wght@600&family=Roboto:wght@400&display=swap">
<style>
  :root {
    --aqua: #a4e4ee;
    --die-line: #3fb8af;
    --paper: #ffffff;
    --brand-blue: #2a9fd8;
    --ribbon-red: #e3232c;
    --ink: #222a30;
    --ink-soft: #4a5258;
  }
  html, body { margin: 0; padding: 0; overflow: hidden; background: var(--paper); }
  .canvas { position: relative; width: 744px; height: 1200px; overflow: hidden; background: var(--paper); font-family: "Roboto", Arial, sans-serif; }
  .dieline { position: absolute; inset: 0; }
  .label { position: absolute; margin: 0; white-space: nowrap; }
  .flipped { transform: rotate(180deg); }
  .fine-print { font-size: 13px; color: var(--ink-soft); }
  .mission { font-family: "Dancing Script", cursive; font-weight: 600; font-size: 38px; color: var(--ink); text-align: center; line-height: 48px; }
  .tagline { font-family: "Courgette", cursive; color: var(--brand-blue); font-size: 32px; font-style: italic; }
  .headline { font-family: "Courgette", cursive; color: var(--brand-blue); font-size: 64px; }
  .brand-seal { position: absolute; width: 128px; height: 128px; border-radius: 50%; background: var(--paper); border: 2px solid var(--ink-soft); display: flex; align-items: center; justify-content: center; font-family: "Courgette", cursive; font-size: 21px; color: var(--ink); }
  .ribbon { position: absolute; width: 164px; height: 44px; display: flex; align-items: center; justify-content: center; font-family: "Courgette", cursive; font-size: 20px; color: var(--paper); }
  .ribbon svg { position: absolute; inset: 0; }
  .ribbon span { position: relative; transform: rotate(-5deg); }
</style>
</head>
<body>
<main class="canvas">
  <svg class="dieline" width="744" height="1200" viewBox="0 0 744 1200" aria-hidden="true">
    <path d="M84,4 H660 C700,60 744,150 744,244 V820 C744,920 680,1000 620,1030 H130 C70,1000 0,920 0,820 V244 C0,150 44,60 84,4Z" fill="var(--aqua)" stroke="var(--die-line)" stroke-width="2"/>
    <g stroke="var(--die-line)" stroke-width="1.5">
      <line x1="0" y1="244" x2="744" y2="244"/>
      <line x1="0" y1="444" x2="744" y2="444"/>
      <line x1="0" y1="636" x2="744" y2="636"/>
      <line x1="0" y1="820" x2="744" y2="820"/>
    </g>
    <rect x="116" y="44" width="144" height="92" fill="none" stroke="var(--ink-soft)" stroke-width="1.5"/>
    <path d="M468,40 H552 L566,110 C590,150 590,200 580,224 H450 C440,200 440,150 462,110Z" fill="var(--paper)" stroke="var(--die-line)" stroke-width="1.5"/>
    <rect x="120" y="238" width="180" height="20" rx="10" fill="var(--paper)" stroke="var(--die-line)" stroke-width="1.5"/>
    <rect x="130" y="820" width="180" height="20" rx="10" fill="var(--paper)" stroke="var(--die-line)" stroke-width="1.5"/>
    <path d="M440,850 H650 C672,900 672,990 640,1020 H470 C428,990 420,900 440,850Z" fill="var(--paper)" stroke="var(--die-line)" stroke-width="1.5"/>
    <rect x="130" y="1030" width="490" height="166" fill="var(--paper)" stroke="var(--die-line)" stroke-width="1.5"/>
    <rect x="144" y="1080" width="166" height="92" fill="none" stroke="var(--ink-soft)" stroke-width="1.5"/>
  </svg>

  <!-- top flap -->
  <p class="label fine-print flipped" style="left:450px; top:14px;">Can be served Frozen or at room temperature</p>
  <p class="label fine-print flipped" style="left:150px; top:80px;">Nutrition Facts</p>
  <p class="label fine-print flipped" style="left:446px; top:206px;">open for cup w/ food to show</p>

  <!-- back panel -->
  <p class="label fine-print flipped" style="left:144px; top:240px; font-size:11px;">open for cup to show</p>
  <div class="brand-seal flipped" style="left:582px; top:276px;">Duo Doxie</div>
  <p class="label mission flipped" style="left:210px; top:302px;">Mission statement is<br>needed here</p>

  <!-- front panel A -->
  <div class="brand-seal" style="left:88px; top:466px;">Duo Doxie</div>
  <p class="label tagline" style="left:220px; top:460px;">Served Frozen or Room Temp</p>
  <p class="label tagline" style="left:240px; top:506px;">4 Individual cups</p>
  <div class="ribbon" style="left:528px; top:502px;">
    <svg viewBox="0 0 164 44" width="164" height="44"><path d="M0,10 L150,0 L164,30 L10,44 L16,26Z" fill="var(--ribbon-red)"/></svg>
    <span>Vacuum Seal</span>
  </div>
  <p class="label headline" style="left:246px; top:536px;">Dog Treats</p>

  <!-- front panel B -->
  <div class="brand-seal" style="left:80px; top:652px;">Duo Doxie</div>
  <p class="label tagline" style="left:220px; top:640px;">Served Frozen or Room Temp</p>
  <p class="label tagline" style="left:240px; top:686px;">4 Individual cups</p>
  <div class="ribbon" style="left:528px; top:682px;">
    <svg viewBox="0 0 164 44" width="164" height="44"><path d="M0,10 L150,0 L164,30 L10,44 L16,26Z" fill="var(--ribbon-red)"/></svg>
    <span>Vacuum Seal</span>
  </div>
  <p class="label headline" style="left:246px; top:716px;">Dog Treats</p>

  <!-- bottom flap -->
  <p class="label fine-print" style="left:154px; top:823px; font-size:11px;">open for cup to show</p>
  <p class="label fine-print" style="left:432px; top:864px;">open for cup w/ food to show</p>
  <p class="label fine-print" style="left:156px; top:1098px;">Spot for Barcode</p>
</main>
</body>
</html>
```